Harbourgate Earthmoving – Website Design Brief

Web Design Brief

We are seeking a web designer to build a modern, responsive website for Harbourgate Earthmoving, a Sydney-based earthworks and excavation company.

2. Project Goal
- Build a professional, easy-to-navigate website that:
- Showcases HGE’s capabilities and past projects
- Attracts residential and commercial developers
- Builds credibility and encourages enquiries

3. Target Audience
- Residential developers and home builders
- Commercial construction firms
- Project managers seeking reliable excavation & plant hire services

4. Services to Highlight
- Bulk Excavation
- Detailed Excavation
- Demolition
- Shoring
- Plant Hire

5. Brand Style & Tone
- Clean, bold, and modern
- Professional with a “we get the job done” attitude
- Colors: Lime Green + Concrete Grey (from logo)
- Fonts: Match the modern, rounded, bold typeface in the logo
- Imagery: Showcase big machines, on-site work, before & after shots

6. Website Pages
Recommended structure:
- Home – Quick intro, project highlights, CTA
- About Us – Team story, mission, safety focus
- Services – Separate sections for each core service
- Projects – Case studies or photo gallery
- Plant Hire – Machines available, specs/photos
- Contact – Form + map + details

7. Assets Provided
- Logo (both long + stacked formats)
- Project photos. More can be provided if required.
- Copy: To be drafted

8. Deliverables
Responsive website (desktop/mobile/tablet)
- SEO-ready structure
- CMS (WordPress) for future edits
- Google Maps integration, job enquiry form

Target Market(s)

Target Audience Residential developers and home builders Commercial construction firms Project managers seeking reliable excavation & plant hire services

Industry/Entity Type

Construction

Number of Pages Required

1 page

Requirements
Must have
• Build a professional, easy-to-navigate website that: Showcases HGE’s capabilities and past projects Attracts residential and commercial developers Builds credibility and encourages enquiries
Nice to have
• All provided in the Description
Should not have

```html
<!DOCTYPE html>
<html lang="en">
<head>
<meta charset="utf-8">
<title>Harbourgate Earthmoving – Sydney Earthworks &amp; Excavation</title>
<link href="https://fonts.googleapis.com/css2?family=Archivo:wght@700;800&family=Poppins:wght@400;500;600&display=swap" rel="stylesheet">
<style>
:root{
  --green:#7cc242;
  --green-dark:#5f9e2c;
  --grey:#8b8b8d;
  --grey-light:#c9c9cb;
  --grey-dark:#4d4d4f;
  --ink:#3a3a3a;
  --muted:#7a7a7a;
  --white:#ffffff;
  --head:'Archivo',sans-serif;
  --body:'Poppins',sans-serif;
}
*{margin:0;padding:0;box-sizing:border-box}
html,body{width:1200px;height:4295px;overflow:hidden}
body{position:relative;font-family:var(--body);color:var(--ink);background:var(--white)}
.abs{position:absolute}
h1,h2,h3,h4{font-family:var(--head);font-weight:800;text-transform:uppercase;color:var(--grey-dark);letter-spacing:.5px}
.btn{display:inline-block;font-family:var(--body);font-weight:600;font-size:11px;border-radius:20px;padding:8px 18px;color:var(--white);background:var(--green);text-decoration:none}
.btn.grey{background:var(--grey)}
.btn.white{background:var(--white);color:var(--ink)}
.photo{border-radius:16px;overflow:hidden}

/* header */
.site-header{top:0;left:0;width:1200px;height:66px}
.brand{left:93px;top:20px;font-family:var(--head);font-weight:800;font-size:21px;letter-spacing:2px;color:var(--green);text-transform:uppercase}
.nav{right:95px;top:21px;display:flex;align-items:center;gap:27px;font-size:11.5px;font-weight:500;color:var(--grey-dark)}
.nav .btn{padding:8px 18px}

/* hero */
.hero-bg{top:0;left:0;width:1200px;height:1240px;background:linear-gradient(180deg,#fff 0,#f6f6f6 330px,#e6e6e6 460px,var(--grey) 640px,#9a9a9c 1000px,#a2a2a4 1240px)}
.hero-trees{top:430px;left:0;width:1200px;height:190px;background:linear-gradient(180deg,rgba(124,194,66,0) 0,rgba(124,194,66,.55) 40%,var(--green) 70%,#8da07a 100%)}
.hero-title{left:93px;top:193px;font-size:35px;line-height:42px;letter-spacing:0}
.hero-title span{color:var(--green)}
.hero-sub{left:93px;top:325px;width:500px;font-size:12.5px;line-height:20px;color:var(--grey-dark)}
.hero-cta{left:93px;top:380px;display:flex;gap:8px}
.hero-arm{left:690px;top:133px;width:200px;height:240px;border-radius:30px 30px 10px 10px;background:linear-gradient(180deg,var(--green),#6aa83a)}
.hero-machine{left:605px;top:330px;width:550px;height:380px;border-radius:30px;background:linear-gradient(180deg,#7cc242 0,#5f9e2c 45%,#5b5b55 100%)}
.play{left:895px;top:222px;width:98px;height:98px;border-radius:50%;background:rgba(130,130,130,.9)}
.see-us{left:1008px;top:253px;font-family:var(--head);font-weight:800;font-size:17px;line-height:19px;color:var(--grey)}

.why-title{top:792px;left:0;width:1200px;text-align:center;color:var(--white);font-size:29px}
.why-cards{left:212px;top:853px;display:flex;gap:10px}
.why-card{width:253px;height:250px;background:var(--white);border-radius:20px;text-align:center;padding:34px 22px 0}
.why-card svg{width:80px;height:80px}
.why-card h3{font-size:15px;line-height:18px;margin-top:10px;color:var(--grey-dark)}
.why-card p{font-size:11.5px;line-height:19px;color:var(--muted);margin-top:6px}
.edge{left:0;width:1200px}

/* services */
.services-title{top:1330px;left:0;width:1200px;text-align:center;font-size:30px}
.services{left:12px;top:1392px;display:flex;gap:8px}
.service{position:relative;width:230px;height:315px;border-radius:16px}
.service h3{position:absolute;left:0;bottom:30px;width:100%;text-align:center;color:var(--white);font-size:15px}

/* about */
.about-img{left:93px;top:1797px;width:397px;height:473px;border-radius:22px;background:linear-gradient(140deg,#7a6450,#5a4a3c 50%,#9c7a4e)}
.about-img-small{left:413px;top:1868px;width:156px;height:184px;border-radius:14px;background:linear-gradient(180deg,#8a9a9e,#6b6a4c 60%,#4a4233)}
.about-line{left:517px;top:2052px;width:2px;height:200px;background:var(--green)}
.about-kicker{left:637px;top:1841px;font-size:15px;font-weight:600;color:var(--green);text-transform:uppercase}
.about-title{left:637px;top:1867px;font-size:31px;line-height:34px}
.about-text{left:637px;top:1938px;width:470px;font-size:11.5px;line-height:20px;color:var(--grey-dark)}
.about-text p+p{margin-top:12px}
.about-btn{left:637px;top:2102px}

/* work */
.work-bg{top:2200px;left:0;width:1200px;height:755px;background:linear-gradient(180deg,#8bc85a 0,var(--green) 40%,#86c04d 100%)}
.work-title{top:2370px;left:0;width:1200px;text-align:center;color:var(--white);font-size:30px}
.work-sub{top:2410px;left:0;width:1200px;text-align:center;color:var(--white);font-size:12.5px}
.work-main{left:93px;top:2458px;width:462px;height:342px;background:linear-gradient(180deg,#e8eef0 0,#8e8e86 45%,#6a4d36 100%)}
.work-main .cap{position:absolute;left:45px;bottom:42px;color:var(--white)}
.work-main h3{color:var(--white);font-size:15px;line-height:20px}
.work-main p{font-size:11px;line-height:16px;width:320px;margin-top:4px}
.work-mid{left:567px;top:2458px;width:263px;height:342px;background:linear-gradient(180deg,#6b84a6,#7a6a5c 60%,#4c4038)}
.work-r1{left:842px;top:2458px;width:262px;height:167px;background:linear-gradient(180deg,#f2f4f6,#d3a15a 60%,#a06a44)}
.work-r2{left:842px;top:2633px;width:262px;height:167px;background:linear-gradient(180deg,#c6d8ea,#c7a35a 55%,#8a6552)}
.work-btn{left:527px;top:2828px;padding:8px 26px}

/* hire */
.hire-title{left:95px;top:3064px;font-size:30px;line-height:34px}
.hire-text{left:93px;top:3140px;width:400px;font-size:11.5px;line-height:18px;color:var(--grey-dark)}
.hire-link{left:93px;top:3183px;font-size:11.5px;font-weight:600;color:var(--green);text-decoration:underline}
.machine{width:233px;height:283px;border-radius:14px;background:var(--white);box-shadow:0 4px 14px rgba(0,0,0,.12);overflow:hidden;text-align:center}
.machine .pic{height:200px}
.machine h4{font-size:14px;line-height:18px;margin-top:24px}
.testimonial{left:608px;top:3070px;width:497px;height:437px;border-radius:38px;background:#f1f1f1;border:1px solid #e6e6e6;text-align:center}
.testimonial h3{font-size:29px;margin-top:10px}
.testimonial p{font-size:14.5px;line-height:24px;color:var(--muted);margin-top:14px}
.testimonial .who{font-weight:600;color:var(--grey-dark);font-size:13.5px;margin-top:10px}
.dots{display:flex;gap:6px;justify-content:center;margin-top:16px}
.dots i{width:8px;height:8px;border-radius:50%;background:#c8c8c8}
.dots i:first-child{background:var(--green)}

/* cta */
.cta-title{top:3605px;left:0;width:1200px;text-align:center;font-size:29px}
.cta-sub{top:3650px;left:0;width:1200px;text-align:center;font-size:12px;color:var(--grey-dark)}
.cta-btns{left:0;width:1200px;top:3687px;display:flex;gap:6px;justify-content:center}
.cta-btns .btn{padding:8px 32px}

/* footer */
.footer-scene{left:0;top:3717px;width:1200px;height:220px;background:linear-gradient(180deg,rgba(90,90,90,0) 0,rgba(90,90,90,.45) 45%,#595959 100%)}
.footer{left:0;top:3900px;width:1200px;height:395px;background:linear-gradient(180deg,#5a5a5a,#4a4a4a)}
.footer-brand{left:147px;top:4008px;font-family:var(--head);font-weight:800;font-size:30px;line-height:38px;color:var(--green);text-transform:uppercase;letter-spacing:1px}
.f-col h4{color:var(--white);font-size:18px}
.f-links{left:432px;top:3995px}
.f-info{left:645px;top:3995px}
.f-list{list-style:none;margin-top:10px;font-size:12px;line-height:22.5px;color:#e4e4e4}
.f-list li{display:flex;align-items:center;gap:6px}
.f-list svg{width:11px;height:11px}
.social{left:928px;top:4055px;display:flex;gap:14px}
.social i{width:28px;height:28px;border-radius:50%;border:1.5px solid #bdbdbd;display:block}
.copyright{left:0;top:4257px;width:1200px;text-align:center;font-size:12px;color:#dcdcdc}
.to-top{left:1127px;top:4222px;width:32px;height:32px;border-radius:50%;background:var(--green)}
</style>
</head>
<body>

<div class="abs hero-bg"></div>
<div class="abs hero-trees" role="img" aria-label="Green silhouette of bushland and power pylons along the skyline"></div>

<header class="abs site-header">
  <div class="abs brand">Harbourgate Earthmoving</div>
  <nav class="abs nav">
    <svg width="13" height="13" viewBox="0 0 16 16"><path d="M8 1 1 7.5h2V15h4v-4h2v4h4V7.5h2z" fill="#7cc242"/></svg>
    <span>About</span><span>Services</span><span>Projects</span><span>Plant Hire</span><span>Contact</span>
    <a class="btn" href="#">Get a Quote</a>
  </nav>
</header>

<h1 class="abs hero-title">Sydney’s<br><span>Trusted</span> Earthworks<br>&amp; Excavation Experts</h1>
<p class="abs hero-sub">Delivering reliable, high-performance excavation services for residential and commercial developments across Sydney.</p>
<div class="abs hero-cta">
  <a class="btn" href="#">View Our Work</a>
  <a class="btn grey" href="#">➊ Get a Free Quote</a>
</div>

<div class="abs hero-arm" role="img" aria-label="Raised boom arm of a lime green excavator"></div>
<div class="abs hero-machine" role="img" aria-label="Lime green excavator with its bucket lowered over a dotted map of Australia"></div>
<div class="abs play"><svg width="98" height="98" viewBox="0 0 98 98"><path d="M40 32v34l28-17z" fill="#fff"/></svg></div>
<div class="abs see-us">SEE US<br>IN ACTION</div>

<h2 class="abs why-title">Why Choose Harbourgate Earthmoving?</h2>
<div class="abs why-cards">
  <div class="why-card">
    <svg viewBox="0 0 80 80" fill="none" stroke="#6a6a6a" stroke-width="2.5"><circle cx="36" cy="40" r="20"/><circle cx="36" cy="40" r="9"/><rect x="46" y="32" width="22" height="20" rx="4" fill="#7cc242" stroke="none"/></svg>
    <h3>Reliable Equipment<br>&amp; Operators</h3>
    <p>Modern machinery and skilled professionals for every job.</p>
  </div>
  <div class="why-card">
    <svg viewBox="0 0 80 80" fill="none" stroke="#6a6a6a" stroke-width="2.5"><path d="M12 46l14-10 14 8 14-8 14 10-14 12-14-6-14 6z"/><path d="M32 10h16v12c0 6-8 10-8 10s-8-4-8-10z" fill="#7cc242" stroke="none"/></svg>
    <h3>Commitment<br>to Safety</h3>
    <p>Strict safety protocols ensure safe work for everyone.</p>
  </div>
  <div class="why-card">
    <svg viewBox="0 0 80 80" fill="none" stroke="#6a6a6a" stroke-width="2.5"><circle cx="40" cy="18" r="10" fill="#7cc242" stroke="none"/><circle cx="40" cy="46" r="8"/><path d="M24 72c0-10 7-16 16-16s16 6 16 16"/><path d="M14 44l3 6 6 1-5 4 1 6-5-3-5 3 1-6-5-4 6-1zM66 44l3 6 6 1-5 4 1 6-5-3-5 3 1-6-5-4 6-1z"/></svg>
    <h3>Years of Proven<br>Experience</h3>
    <p>From small digs to major developments, we’ve done it all.</p>
  </div>
</div>

<svg class="abs edge" style="top:1180px" height="80" viewBox="0 0 1200 80" preserveAspectRatio="none"><path d="M0 0H1200V60L1170 48 1140 62 1100 40 1060 55 1020 30 990 50 940 35 900 58 860 42 820 50 780 28 740 52 700 38 650 55 610 40 570 58 530 36 490 50 450 30 410 55 370 44 330 60 290 40 250 52 210 34 170 56 130 45 90 62 50 42 20 58 0 70Z" fill="#a2a2a4"/></svg>

<h2 class="abs services-title">What We Do</h2>
<div class="abs services">
  <div class="service" role="img" aria-label="Excavator on a bulk excavation site" style="background:linear-gradient(180deg,#9ab4c8,#a8744a 55%,#3a2e28)"><h3>Bulk Excavation</h3></div>
  <div class="service" role="img" aria-label="Orange excavator working in a rocky quarry" style="background:linear-gradient(180deg,#7d8c8a,#b9663a 50%,#2f2f2f)"><h3>Detailed Excavation</h3></div>
  <div class="service" role="img" aria-label="Excavator bucket tearing down a structure" style="background:linear-gradient(180deg,#c7d6e2,#4e8a86 40%,#2b2622)"><h3>Demolition</h3></div>
  <div class="service" role="img" aria-label="Worker inspecting steel shoring reinforcement" style="background:linear-gradient(180deg,#8b6048,#4a5a6e 55%,#2a2a34)"><h3>Shoring</h3></div>
  <div class="service" role="img" aria-label="Backhoe loader available for plant hire" style="background:linear-gradient(180deg,#8fb6d8,#b58e48 55%,#2e2a26)"><h3>Plant Hire</h3></div>
</div>

<div class="abs work-bg" role="img" aria-label="Green tinted backdrop of earthmoving machines on site"></div>
<svg class="abs edge" style="top:2180px" height="90" viewBox="0 0 1200 90" preserveAspectRatio="none"><path d="M0 30L40 20 70 42 110 26 150 45 200 28 240 40 290 24 330 42 380 30 430 48 480 35 520 46 560 22 600 40 650 30 700 44 760 26 800 40 850 10 880 30 920 22 960 40 1010 28 1060 44 1110 26 1160 40 1200 30V90H0Z" fill="#8bc85a"/></svg>

<div class="abs about-img" role="img" aria-label="Aerial view of an orange excavator digging a dirt site"></div>
<div class="abs about-line"></div>
<div class="abs about-img-small" role="img" aria-label="Excavator loading a truck beside a pylon"></div>
<div class="abs about-kicker">About Us</div>
<h2 class="abs about-title">Built on Experience.<br>Driven by Results.</h2>
<div class="abs about-text">
  <p>At Harbourgate Earthmoving, we bring decades of combined experience to every excavation and earthworks project across Sydney. As a locally owned and operated company, we understand the terrain, timelines, and expectations of both residential and commercial developers.</p>
  <p>We’ve built our reputation on precision, performance, and a “get the job done” attitude. Whether it’s a complex bulk excavation, a detailed dig, or plant hire for your site—we deliver with efficiency and integrity.</p>
</div>
<a class="abs btn about-btn" href="#">Read More</a>

<h2 class="abs work-title">Our Work in Action</h2>
<p class="abs work-sub">Here’s a look at some of our recent projects across Greater Sydney.</p>
<div class="abs photo work-main" role="img" aria-label="Large house with completed bulk cut and fill pad">
  <div class="cap">
    <h3>Bulk Cut &amp; Fill –<br>Parramatta Development</h3>
    <p>Completed mass excavation and pad preparation for a large residential development in just 3 weeks.</p>
  </div>
</div>
<div class="abs photo work-mid" role="img" aria-label="Partially demolished multi-storey building"></div>
<div class="abs photo work-r1" role="img" aria-label="Yellow excavator on a red earth mound"></div>
<div class="abs photo work-r2" role="img" aria-label="Yellow excavator sorting demolition rubble"></div>
<a class="abs btn white work-btn" href="#">View All Projects</a>

<h2 class="abs hire-title">Hire the Right<br>Machine for the Job</h2>
<p class="abs hire-text">From tight-access mini excavators to heavy machinery, our fleet is ready for action.</p>
<a class="abs hire-link" href="#">Enquire About Availability</a>
<div class="abs machine" style="left:95px;top:3225px">
  <div class="pic" role="img" aria-label="12 tonne excavator pouring soil from its bucket" style="background:linear-gradient(180deg,#6aa8dc,#c99a3a 55%,#8a5a3a)"></div>
  <h4>12T Excavator –<br>GPS-Equipped</h4>
</div>
<div class="abs machine" style="left:337px;top:3225px">
  <div class="pic" role="img" aria-label="White tipper truck parked at a depot" style="background:linear-gradient(180deg,#9aa0a6,#e8e8e8 50%,#6a6a6a)"></div>
  <h4>Tipper Trucks<br>– 10m³</h4>
</div>

<div class="abs testimonial">
  <svg width="60" height="50" viewBox="0 0 60 50" style="margin-top:108px"><path d="M4 48V28C4 14 10 6 24 2l3 6c-7 3-10 8-10 14h10v26zM33 48V28c0-14 6-22 20-26l3 6c-7 3-10 8-10 14h10v26z" fill="#7cc242"/></svg>
  <h3>Client Testimonial</h3>
  <p>Harbourgate Earthmoving delivered on time and with precision.<br>Their team made a complex dig feel easy.</p>
  <div class="who">Mark T., Site Manager, Ridgeline Homes</div>
  <div class="dots"><i></i><i></i><i></i></div>
</div>

<h2 class="abs cta-title">Need Reliable Excavation Services?</h2>
<p class="abs cta-sub">Get in touch with our team to discuss your project needs. We’re ready to deliver results.</p>
<div class="abs cta-btns">
  <a class="btn" href="#">Call Now</a>
  <a class="btn grey" href="#" style="padding:8px 16px">➊ Get a Free Quote</a>
</div>

<div class="abs footer-scene" role="img" aria-label="Grey silhouette of excavators and trucks on a construction skyline"></div>
<footer class="abs footer"></footer>
<div class="abs footer-brand">Harbour<br>gate<br>Earthmoving</div>
<div class="abs f-col f-links">
  <h4>Quick Links</h4>
  <ul class="f-list"><li>Home</li><li>About</li><li>Services</li><li>Projects</li><li>Plant Hire</li><li>Contact</li></ul>
</div>
<div class="abs f-col f-info">
  <h4>Company Info</h4>
  <ul class="f-list">
    <li><svg viewBox="0 0 12 12"><path d="M6 0a4 4 0 0 0-4 4c0 3 4 8 4 8s4-5 4-8a4 4 0 0 0-4-4zm0 5.5A1.5 1.5 0 1 1 6 2.5a1.5 1.5 0 0 1 0 3z" fill="#7cc242"/></svg>Harbourgate Earthmoving Pty Ltd</li>
    <li style="padding-left:17px">ABN: 00 000 000 000</li>
    <li style="padding-left:17px">Sydney, NSW</li>
    <li><svg viewBox="0 0 12 12"><rect x="0" y="2" width="12" height="8" rx="1" fill="#7cc242"/><path d="M0 3l6 4 6-4" stroke="#4d4d4f" fill="none"/></svg>info@harbourgateearthmoving.com.au</li>
    <li><svg viewBox="0 0 12 12"><path d="M2.5 0 5 3 3.6 4.6a7 7 0 0 0 3.8 3.8L9 7l3 2.5-1.5 2.2C5 11.5.5 7 .3 1.5z" fill="#7cc242"/></svg>(02) 9000 4821</li>
  </ul>
</div>
<div class="abs social"><i></i><i></i><i></i><i></i></div>
<div class="abs to-top"><svg width="32" height="32" viewBox="0 0 32 32"><path d="M12 18l4-4 4 4" stroke="#fff" stroke-width="2" fill="none"/></svg></div>
<div class="abs copyright">2025 Harbourgate Earthmoving. All rights reserved. | Lic #482019376</div>

</body>
</html>
```